Brisk Meadow Builders needs a product brochure

We need a new flyer for our Patio Perch Lounge. Here is some of the copy your will need.
"Turn your back yard into the ultimate entertianment venue with the stunning Patio Perch Lounge!"
"Entertain family & friends in your very own back yard!"
"Available with or without solar and comes in a variety of colors"
"The Patio Perch Lounge measures 5' deep by 10' wide and is 9'-6" at it's highest point"
"Constructed with treated 4x4's, primed then painted with Thornby Calder best exterior paint for years of care free enjoyment. Also, Marlow Pendt Keystead shingles are dimensional, have a 25 year warranty and are rated for 150 mph winds!"
"TV Mount included. Shelves and TV are sold separately"
There also needs to be a box where we can add the price into later. The price can change from time to time due to material cost fluctuation.
Look and feel
Each slider illustrates characteristics of the customer's brand and the style your logo design should communicate.

```html
<!DOCTYPE html>
<html lang="en">
<head>
<meta charset="utf-8">
<title>Brisk Meadow Builders – Patio Perch Lounge Flyer</title>
<link rel="stylesheet" href="https://fonts.googleapis.com/css2?family=Montserrat:wght@400;500;700;800;900&display=swap">
<style>
  :root {
    --green: #5b9f3b;
    --orange: #f8b124;
    --orange-dark: #e39a12;
    --ink: #2a2a2a;
    --white: #ffffff;
    --backdrop: #e4e5e8;
  }
  * { margin: 0; padding: 0; box-sizing: border-box; }
  html, body {
    width: 1200px; height: 2400px; overflow: hidden;
    background: var(--backdrop);
    font-family: "Montserrat", sans-serif;
  }
  .stage { position: relative; width: 1200px; height: 2400px; }
  .flyer {
    position: absolute; left: 0; top: 351px;
    width: 868px; height: 1228px;
    background: var(--white);
    transform: scale(1.3825); transform-origin: 0 0;
    overflow: hidden;
  }
  .flyer > * { position: absolute; }
  .green-band { left: 0; top: 277px; width: 868px; height: 355px; background: var(--green); }
  .lifestyle-photo {
    left: -205px; top: 88px; width: 584px; height: 584px; border-radius: 50%;
    background: linear-gradient(135deg, #6d8f4a 0%, #3b3e42 30%, #8a5d36 55%, #8c8d8f 100%);
  }
  .brand {
    right: 50px; top: 150px; text-align: right;
    color: var(--green); font-weight: 800; font-size: 30px; line-height: 1.1;
    letter-spacing: 1px; text-transform: uppercase;
  }
  .brand-dot { right: 50px; top: 95px; width: 40px; height: 40px; border-radius: 50%; background: var(--green); }
  .headline { right: 42px; top: 292px; text-align: right; }
  .headline .lead {
    color: var(--white); font-weight: 700; font-size: 22.5px; line-height: 30px; text-transform: uppercase;
  }
  .headline .product { color: var(--orange); font-weight: 900; text-transform: uppercase; line-height: 1; }
  .headline .product-top { font-size: 44px; margin-top: 6px; }
  .headline .product-main { font-size: 74px; letter-spacing: -1px; }
  .product-photo {
    left: 372px; top: 565px; width: 496px; height: 480px;
    background: linear-gradient(180deg, #3a3d40 0%, #3a3d40 18%, #a8713c 34%, #7a5232 55%, #2f3134 70%, #4b4d50 100%);
  }
  .price-box {
    right: 22px; top: 958px; width: 210px; height: 64px;
    background: var(--white); border: 3px solid var(--green); border-radius: 6px;
    display: flex; align-items: center; padding: 0 14px; gap: 10px;
  }
  .price-box .label { color: var(--green); font-weight: 800; font-size: 18px; text-transform: uppercase; }
  .price-box .amount {
    flex: 1; height: 30px; border-bottom: 2px solid var(--orange);
    color: var(--ink); font-weight: 800; font-size: 22px; line-height: 30px;
  }
  .intro { left: 34px; top: 696px; width: 350px; }
  .intro h2 { color: var(--green); font-weight: 800; font-size: 23.5px; line-height: 32px; text-transform: uppercase; }
  .intro p {
    margin-top: 8px; color: var(--ink); font-weight: 400; font-size: 16.5px; line-height: 21px; text-transform: uppercase;
  }
  .specs { left: 34px; top: 886px; display: flex; gap: 8px; }
  .spec {
    width: 111px; height: 111px; border-radius: 50%;
    background: var(--orange); border: 3px solid var(--orange-dark);
    display: flex; flex-direction: column; align-items: center; justify-content: center;
    color: var(--ink); box-shadow: inset 0 0 0 4px #fbc24d;
  }
  .spec strong { font-weight: 800; font-size: 31px; line-height: 1; }
  .spec span { font-weight: 500; font-size: 16px; text-transform: uppercase; margin-top: 2px; }
  .details {
    left: 34px; top: 1010px; width: 330px;
    color: var(--ink); font-size: 13.3px; line-height: 17.4px; text-align: justify; font-weight: 500;
  }
  .note { left: 34px; top: 1132px; color: var(--ink); font-size: 13.3px; line-height: 17.4px; font-weight: 500; }
  .call {
    left: 34px; top: 1177px; width: 320px; height: 28px; background: var(--green);
    display: flex; align-items: center; justify-content: center; gap: 8px;
    font-weight: 900; font-size: 21px; text-transform: uppercase;
  }
  .call .label { color: var(--orange); }
  .call .phone { color: var(--white); }
  .gallery {
    left: 385px; top: 1035px; width: 468px; height: 168px; background: var(--green);
    padding: 9px 6px; display: flex; gap: 5px;
  }
  .gallery .shot { flex: 1; }
  .shot.wine { background: linear-gradient(180deg, #2d2f33 0%, #3b3a3a 45%, #b07040 100%); }
  .shot.spirits { background: linear-gradient(180deg, #a0673a 0%, #2a3038 45%, #1f2a38 80%, #a0673a 100%); }
  .shot.opener { background: linear-gradient(135deg, #9fb58a 0%, #6e7d68 45%, #c98450 100%); }
</style>
</head>
<body>
<div class="stage">
  <article class="flyer">
    <div class="green-band"></div>

    <div class="lifestyle-photo" role="img" aria-label="Photo of friends seated at the backyard bar with a dog at their feet"></div>

    <div class="brand-dot"></div>
    <div class="brand">Brisk Meadow<br>Builders</div>

    <div class="headline">
      <div class="lead">Turn your back yard<br>into the ultimate<br>entertianment venue<br>with the stunning</div>
      <div class="product product-top">Patio Perch</div>
      <div class="product product-main">Lounge!</div>
    </div>

    <div class="product-photo" role="img" aria-label="Photo of the solar-roofed backyard bar with TV, shelves, stools and cooler"></div>

    <div class="price-box"><span class="label">Price</span><span class="amount">$</span></div>

    <section class="intro">
      <h2>Entertain family &amp;<br>friends in your<br>very own back yard!</h2>
      <p>Available with or without<br>solar and comes in a variety<br>of colors</p>
    </section>

    <div class="specs">
      <div class="spec"><strong>5'</strong><span>Deep</span></div>
      <div class="spec"><strong>10'</strong><span>Wide</span></div>
      <div class="spec"><strong>9'6"</strong><span>Height</span></div>
    </div>

    <p class="details">Constructed with treated 4x4's, primed then painted with Thornby Calder best exterior paint for years of care free enjoyment. Also, Marlow Pendt Keystead shingles are dimensional, have a 25 year warranty and are rated for 150 mph winds!</p>

    <p class="note">TV Mount included.<br>Shelves and TV are sold separately</p>

    <div class="call"><span class="label">Call us</span><span class="phone">555-014-2290</span></div>

    <div class="gallery">
      <div class="shot wine" role="img" aria-label="Close-up of wine rack and hanging glasses"></div>
      <div class="shot spirits" role="img" aria-label="Close-up of spirits shelf with glassware"></div>
      <div class="shot opener" role="img" aria-label="Hand using the wall-mounted bottle opener beside a football"></div>
    </div>
  </article>
</div>
</body>
</html>
```